Acupuncture Medspa needs a business card design

I need a business card design that looks professional, has a spa-like quality and can offer a promo on the back. Initial promo is "First session free". The tagline of NeedleNook is: Refresh, Restore, Rejuvenate.

NeedleNook is a membership-based acupuncture medspa that offers acupuncture, cupping, and herbal therapies. Members choose between the "Refresh" membership which is for stress relief, or "Restore" which is for treating health conditions, and lastly "Rejuvenate" which is for natural facial enhancement.

Industry/Entity Type

Health And Wellness

Contact Information for Business Card

Coral Haskins, MAC, L.Ac.
612-555-0193
www.needlenook-example.com

Font styles to use
Serif
Sans Serif

Colors

Designer to choose colors to be used in the design.

Requirements
Must have
• The project must have NeedleNook logo, promo on the back, and contact information
Nice to have
• I would like to see the colors of the logo used.

```html
<!DOCTYPE html>
<html lang="en">
<head>
<meta charset="utf-8">
<title>NeedleNook Business Card</title>
<link rel="stylesheet" href="https://fonts.googleapis.com/css2?family=Montserrat:wght@600;700&family=Questrial&display=swap">
<style>
  :root {
    --teal: #178984;
    --teal-soft: #e6f3f3;
    --brown: #3f2a1f;
    --white: #ffffff;
    --page: #ffffff;
  }
  * { margin: 0; padding: 0; box-sizing: border-box; }
  html, body { width: 1000px; height: 1200px; overflow: hidden; background: var(--page); }
  .canvas { position: relative; width: 1000px; height: 1200px; }

  .card { position: absolute; left: 170px; width: 660px; height: 428px; border-radius: 64px; overflow: hidden; }
  .card-front { top: 130px; background: var(--white); border: 1.2px solid var(--teal); }
  .card-back { top: 641px; background: var(--teal); }

  .front-art { position: absolute; left: -1px; top: -1px; width: 660px; height: 428px; }

  .brand {
    position: absolute; right: 28px; top: 70px;
    display: flex; align-items: center; gap: 14px;
    font-family: "Montserrat", sans-serif; font-weight: 600;
    font-size: 44px; color: var(--teal); letter-spacing: 0.5px;
  }
  .brand-dot { width: 16px; height: 16px; border-radius: 50%; background: var(--teal); }

  .holder {
    position: absolute; right: 26px; top: 260px;
    font-family: "Montserrat", sans-serif; font-weight: 700;
    font-size: 25px; color: var(--brown); letter-spacing: -0.3px;
  }
  .contact { position: absolute; right: 26px; top: 318px; list-style: none; }
  .contact li {
    display: flex; justify-content: flex-end; align-items: center; gap: 12px;
    font-family: "Montserrat", sans-serif; font-weight: 700; color: var(--brown);
    height: 26px;
  }
  .contact .phone { font-size: 16px; letter-spacing: 2.6px; }
  .contact .web { font-size: 15.5px; }
  .contact svg { width: 24px; height: 20px; flex: none; }

  .promo, .tagline {
    position: absolute; left: 0; text-align: center;
    font-family: "Questrial", sans-serif; color: var(--white);
  }
  .promo { top: 14px; width: 630px; font-size: 25px; }
  .tagline { top: 376px; width: 650px; font-size: 27px; }
  .tagline .sep { margin: 0 20px 0 14px; }

  .back-mark {
    position: absolute; left: 170px; top: 82px; width: 290px; height: 290px;
    border: 6px solid var(--white); border-radius: 50%;
    display: flex; align-items: center; justify-content: center;
    font-family: "Montserrat", sans-serif; font-weight: 600; font-size: 40px; color: var(--white);
  }
</style>
</head>
<body>
<main class="canvas">

  <section class="card card-front" aria-label="Card front">
    <svg class="front-art" viewBox="0 0 660 428">
      <defs>
        <radialGradient id="softGlow" cx="0.5" cy="0.5" r="0.5">
          <stop offset="0" stop-color="var(--teal-soft)"/>
          <stop offset="0.7" stop-color="var(--teal-soft)" stop-opacity="0.8"/>
          <stop offset="1" stop-color="var(--teal-soft)" stop-opacity="0"/>
        </radialGradient>
      </defs>
      <ellipse role="img" aria-label="Soft decorative backdrop area" cx="200" cy="220" rx="150" ry="190" fill="url(#softGlow)"/>
      <path d="M0 50 C20 240 140 360 325 428 L0 428 Z" fill="var(--brown)"/>
      <path d="M0 50 C16 240 130 360 290 428 L0 428 Z" fill="var(--teal)"/>
    </svg>

    <div class="brand"><span class="brand-dot"></span>NeedleNook</div>

    <h1 class="holder">Coral Haskins, MAC, L.Ac.</h1>
    <ul class="contact">
      <li class="phone">612-555-0193
        <svg viewBox="0 0 24 20" aria-hidden="true"><path d="M6 2 L9 6 L7.5 8 C8.5 10.5 10.5 12.5 13 13.5 L15 12 L19 15 L17 18 C10 18 3 11 3 4 Z" fill="none" stroke="var(--teal)" stroke-width="1.8" stroke-linejoin="round"/><path d="M14 3 A6 6 0 0 1 19 8 M14 0.5 A8.5 8.5 0 0 1 21.5 8" fill="none" stroke="var(--teal)" stroke-width="1.5"/></svg>
      </li>
      <li class="web">www.needlenook-example.com
        <svg viewBox="0 0 24 20" aria-hidden="true"><rect x="2" y="4" width="20" height="13" fill="none" stroke="var(--teal)" stroke-width="1.8"/><path d="M2 4 L12 12 L22 4 M2 17 L9 10 M22 17 L15 10" fill="none" stroke="var(--teal)" stroke-width="1.5"/></svg>
      </li>
    </ul>
  </section>

  <section class="card card-back" aria-label="Card back">
    <p class="promo">The first session free</p>
    <div class="back-mark">NeedleNook</div>
    <p class="tagline">Refresh<span class="sep">|</span>Restore<span class="sep">|</span>Rejuvenate</p>
  </section>

</main>
</body>
</html>
```